Bref créative
Holy Brambleton Chapel Stationary
Fr. Gerald Brint
Professional
pastor
415 Pinecrest Dr. West
Oakville, ON K2R 8W4
pastor@hbcvx.ca
www.hbcvx.ca
I think the Letterhead will work better is offset to the right corner so that the left side of the page could still be used for typing date, address, etc.. However, open to other ideas.
use map provided in download section. I will try to get the ai file shortly.
The wave is okay, but it cannot touch the edge of the paper.
Please use the map in the top left corner. Thx

```html
<!DOCTYPE html>
<html lang="en">
<head>
<meta charset="utf-8">
<title>Holy Brambleton Chapel Stationery</title>
<link href="https://fonts.googleapis.com/css2?family=Cormorant+Garamond:wght@600&family=Open+Sans:wght@400&display=swap" rel="stylesheet">
<style>
:root{
  --backdrop:#d8d8d8;
  --paper:#ffffff;
  --brown:#5a4335;
  --brown-soft:#8a7467;
  --faint:#efeceb;
  --label:#666;
}
*{margin:0;padding:0;box-sizing:border-box}
html,body{width:1200px;height:418px;overflow:hidden;background:var(--backdrop)}
body{position:relative;font-family:"Open Sans",Arial,sans-serif}
.piece{position:absolute;background:var(--paper);box-shadow:0 1px 3px rgba(0,0,0,.25);overflow:hidden}
.piece-label{position:absolute;font-size:5px;color:var(--label);white-space:nowrap;transform:translateX(-50%)}
.wave{position:absolute;left:0;bottom:0;width:100%}
.brand{position:absolute;display:flex;flex-direction:column;align-items:center;font-family:"Cormorant Garamond",Georgia,serif;font-weight:600;color:var(--brown);line-height:1.05;text-align:center}
.brand-mark{width:9px;height:9px;background:var(--brown);margin-bottom:2px}
.brand-name{font-size:7px}
.letterhead{width:204px;height:276px;top:120px}
.letterhead .brand{top:12px;right:12px}
.watermark{position:absolute;left:0;right:0;top:110px;text-align:center;font-family:"Cormorant Garamond",Georgia,serif;font-weight:600;font-size:17px;color:var(--faint)}
.contact{position:absolute;right:10px;bottom:8px;font-size:3.6px;line-height:1.45;color:var(--paper);text-align:left}
.foot-brand{position:absolute;left:14px;bottom:8px;font-family:"Cormorant Garamond",Georgia,serif;font-weight:600;font-size:5px;color:var(--paper)}
.card{width:78px;height:43px;top:29px}
.card-front .brand{left:0;right:0;top:8px}
.card-back{background:var(--brown)}
.card-back .brand{left:0;right:0;top:10px;color:var(--paper)}
.card-back .brand-mark{background:var(--paper)}
.envelope{width:226px;height:110px}
.envelope .brand{left:14px;top:10px}
.envelope .return{position:absolute;left:14px;top:34px;font-size:3.6px;line-height:1.45;color:var(--brown)}
.envelope-back .flap{position:absolute;inset:0}
</style>
</head>
<body>
<svg width="0" height="0" style="position:absolute" aria-hidden="true">
  <defs>
    <symbol id="wave-band" viewBox="0 0 200 40" preserveAspectRatio="none">
      <path d="M0,14 C50,-2 110,28 200,4" fill="none" stroke="#8a7467" stroke-width="0.8"/>
      <path d="M0,20 C55,4 115,32 200,10 L200,40 L0,40 Z" fill="#5a4335"/>
    </symbol>
  </defs>
</svg>

<!-- Letterheads -->
<span class="piece-label" style="left:121px;top:112px">Letterhead one</span>
<section class="piece letterhead" style="left:19px">
  <div class="brand"><span class="brand-mark"></span><span class="brand-name">Holy Brambleton<br>Chapel</span></div>
  <div class="watermark">Holy Brambleton Chapel</div>
  <svg class="wave" height="44"><use href="#wave-band"/></svg>
  <div class="foot-brand">Holy Brambleton Chapel</div>
  <address class="contact" style="font-style:normal">Fr. Gerald Brint, pastor<br>415 Pinecrest Dr. West<br>Oakville, ON K2R 8W4<br>pastor@hbcvx.ca · www.hbcvx.ca</address>
</section>

<span class="piece-label" style="left:342px;top:112px">Letterhead two</span>
<section class="piece letterhead" style="left:240px">
  <div class="brand"><span class="brand-mark"></span><span class="brand-name">Holy Brambleton<br>Chapel</span></div>
  <div class="watermark">Holy Brambleton Chapel</div>
  <svg class="wave" height="44"><use href="#wave-band"/></svg>
  <div class="foot-brand">Holy Brambleton Chapel</div>
  <address class="contact" style="font-style:normal">Fr. Gerald Brint, pastor<br>415 Pinecrest Dr. West<br>Oakville, ON K2R 8W4<br>pastor@hbcvx.ca · www.hbcvx.ca</address>
</section>

<span class="piece-label" style="left:570px;top:112px">Letterhead three</span>
<section class="piece letterhead" style="left:468px">
  <div class="brand"><span class="brand-mark"></span><span class="brand-name">Holy Brambleton<br>Chapel</span></div>
  <div class="watermark">Holy Brambleton Chapel</div>
  <svg class="wave" height="44"><use href="#wave-band"/></svg>
  <div class="foot-brand">Holy Brambleton Chapel</div>
  <address class="contact" style="font-style:normal">Fr. Gerald Brint, pastor<br>415 Pinecrest Dr. West<br>Oakville, ON K2R 8W4<br>pastor@hbcvx.ca · www.hbcvx.ca</address>
</section>

<!-- Business cards -->
<span class="piece-label" style="left:519px;top:21px">Card front</span>
<section class="piece card card-front" style="left:480px">
  <div class="brand"><span class="brand-mark"></span><span class="brand-name">Holy Brambleton<br>Chapel</span></div>
  <svg class="wave" height="8"><use href="#wave-band"/></svg>
</section>
<span class="piece-label" style="left:603px;top:21px">Card back</span>
<section class="piece card card-back" style="left:564px">
  <div class="brand"><span class="brand-mark"></span><span class="brand-name">Holy Brambleton<br>Chapel</span></div>
</section>

<!-- Envelopes -->
<span class="piece-label" style="left:816px;top:21px">Envelope one</span>
<section class="piece envelope" style="left:703px;top:29px">
  <div class="brand"><span class="brand-mark"></span><span class="brand-name">Holy Brambleton<br>Chapel</span></div>
  <address class="return" style="font-style:normal">415 Pinecrest Dr. West<br>Oakville, ON K2R 8W4</address>
  <svg class="wave" height="22"><use href="#wave-band"/></svg>
</section>
<span class="piece-label" style="left:1056px;top:21px">Envelope two</span>
<section class="piece envelope" style="left:943px;top:29px">
  <div class="brand"><span class="brand-mark"></span><span class="brand-name">Holy Brambleton<br>Chapel</span></div>
  <address class="return" style="font-style:normal">415 Pinecrest Dr. West<br>Oakville, ON K2R 8W4</address>
  <svg class="wave" height="22"><use href="#wave-band"/></svg>
</section>
<span class="piece-label" style="left:816px;top:148px">Envelope three</span>
<section class="piece envelope" style="left:703px;top:156px">
  <div class="brand"><span class="brand-mark"></span><span class="brand-name">Holy Brambleton<br>Chapel</span></div>
  <address class="return" style="font-style:normal">415 Pinecrest Dr. West<br>Oakville, ON K2R 8W4</address>
  <svg class="wave" height="22"><use href="#wave-band"/></svg>
</section>
<span class="piece-label" style="left:1056px;top:148px">Envelope four</span>
<section class="piece envelope" style="left:943px;top:156px">
  <div class="brand"><span class="brand-mark"></span><span class="brand-name">Holy Brambleton<br>Chapel</span></div>
  <address class="return" style="font-style:normal">415 Pinecrest Dr. West<br>Oakville, ON K2R 8W4</address>
  <svg class="wave" height="22"><use href="#wave-band"/></svg>
</section>
<span class="piece-label" style="left:816px;top:280px">Envelope back</span>
<section class="piece envelope envelope-back" style="left:703px;top:288px">
  <svg class="flap" viewBox="0 0 226 110" preserveAspectRatio="none">
    <path d="M0,0 L113,58 L226,0" fill="none" stroke="#cfc8c4" stroke-width="0.8"/>
  </svg>
  <svg class="wave" height="18"><use href="#wave-band"/></svg>
</section>
</body>
</html>
```